The Brightwater Compass Business Card

We need an attractive business card with the logo that we bought from ArtVantly last year.
Our mission is to contribute to change the way today's leaders manage business companies bringing value to the workplace and helping them to build a new model of creating wealth.
Our logo is clear about our values : we seek Positive Change through People and are convinced that the pursuit of individual well-being and the chase of economic results can converge with the right management.
Management Consulting
Corinne Fabrelle
+34 612 98 70 31
corinne.fabrelle@thebrightwatercompass-mail.net
www.thebrightwatercompass-mail.net

```html
<!DOCTYPE html>
<html lang="en">
<head>
<meta charset="utf-8">
<title>The Brightwater Compass – Business Card</title>
<link rel="stylesheet" href="https://fonts.googleapis.com/css2?family=Alegreya+SC:wght@500&family=Lato:wght@400&display=swap">
<style>
  :root {
    --backdrop: #ecebea;
    --card-face: #f7f6f5;
    --teal-deep: #047f7b;
    --teal-bright: #05a88f;
    --logo-teal: #13807a;
    --logo-faint: #8cc3be;
    --ink-light: #ffffff;
  }
  html, body {
    margin: 0;
    width: 1200px;
    height: 900px;
    overflow: hidden;
    background: var(--backdrop);
  }
  .canvas {
    position: relative;
    width: 1200px;
    height: 900px;
  }
  .card {
    position: absolute;
    background: var(--card-face);
    box-shadow: 0 6px 18px rgba(0,0,0,0.12);
    overflow: hidden;
  }
  .card--front { left: 78px; top: 103px; width: 587px; height: 364px; }
  .card--back  { left: 388px; top: 505px; width: 567px; height: 352px; }

  .brand {
    position: absolute;
    left: 0; right: 0;
    display: flex;
    flex-direction: column;
    align-items: center;
    gap: 16px;
  }
  .card--front .brand { top: 46px; }
  .card--back .brand  { top: 42px; transform: scaleX(-1); }
  .brand__mark {
    width: 56px; height: 56px;
    border-radius: 50%;
    background: var(--logo-teal);
  }
  .brand__name {
    font-family: "Alegreya SC", serif;
    font-weight: 500;
    font-size: 34px;
    letter-spacing: 0.5px;
    color: var(--logo-teal);
    margin: 0;
  }
  .card--back .brand__mark { background: var(--logo-faint); }
  .card--back .brand__name { color: var(--logo-faint); }

  .band {
    position: absolute;
    left: 0; right: 0; bottom: 0;
    display: flex;
    flex-direction: column;
    align-items: center;
    justify-content: center;
    color: var(--ink-light);
    font-family: "Lato", sans-serif;
  }
  .card--front .band { height: 147px; background: var(--teal-deep); }
  .card--back .band  { height: 139px; background: var(--teal-bright); }

  .contact__name {
    font-family: "Alegreya SC", serif;
    font-weight: 500;
    font-size: 27px;
    letter-spacing: 1px;
    margin: 0 0 14px;
  }
  .contact__line {
    font-size: 15px;
    line-height: 22px;
    margin: 0;
  }
  .website { font-size: 16px; margin: 0; }
</style>
</head>
<body>
<main class="canvas">
  <section class="card card--front" aria-label="Business card front">
    <div class="brand">
      <span class="brand__mark" aria-hidden="true"></span>
      <p class="brand__name">The Brightwater Compass</p>
    </div>
    <div class="band">
      <p class="contact__name">Corinne Fabrelle</p>
      <p class="contact__line">+34 612 98 70 31</p>
      <p class="contact__line">corinne.fabrelle@thebrightwatercompass-mail.net</p>
    </div>
  </section>

  <section class="card card--back" aria-label="Business card back">
    <div class="brand" aria-hidden="true">
      <span class="brand__mark"></span>
      <p class="brand__name">The Brightwater Compass</p>
    </div>
    <div class="band">
      <p class="website">www.thebrightwatercompass-mail.net</p>
    </div>
  </section>
</main>
</body>
</html>
```